Labels for probiotic care products as Body Cream, Shower gel, Hand soap, ....

We are a starting a business in Flanders Belgium. We are looking for a label for care products, based on probiotics or good bacterie. We are looking for a fresh design that attracts people who wants a good product, based on naturally components. The products make that the microflora of the skin becomes and remains natural. The label must we be adaptive on bottles of 15 cm height to 8 cm height and a width of 4,5 cm. The brand name is KOVA REMU (beautiful skin in Hawaiian) or maybe just KOVA.

Industry/Entity Type

Business

Colors

Designer to choose colors to be used in the design.

Requirements
Must have
• somewhere the text "Probiotic Skin Care"
• I also have to tell that the bottles are white.
Nice to have
• I uploaded the 9 existing labels, but I want a totally new one, because the labels of our cleaning products are the same. I also uploaded a mood bord of labels I like.

```html
<!DOCTYPE html>
<html lang="en">
<head>
<meta charset="utf-8">
<title>KOVA Natural Skin Cream Label</title>
<link rel="stylesheet" href="https://fonts.googleapis.com/css2?family=Montserrat:wght@400;600;700;800&display=swap">
<style>
  :root {
    --page: #ffffff;
    --label: #d9a24e;
    --label-shade: #cf9845;
    --green-dark: #2f7d2e;
    --green-band-start: #c6dc2a;
    --green-band-end: #5fa23a;
    --white: #ffffff;
    --ink: #4a4030;
    --faint: rgba(255, 255, 255, 0.35);
  }
  html, body {
    margin: 0;
    padding: 0;
    width: 1200px;
    height: 900px;
    overflow: hidden;
    background: var(--page);
    font-family: "Montserrat", sans-serif;
  }
  .canvas {
    position: relative;
    width: 1200px;
    height: 900px;
  }
  .label {
    position: absolute;
    left: 420px;
    top: 60px;
    width: 360px;
    height: 780px;
    background: linear-gradient(90deg, var(--label-shade), var(--label) 30%, var(--label) 75%, var(--label-shade));
    border-radius: 6px;
    overflow: hidden;
  }
  .brand-mark {
    position: absolute;
    top: 150px;
    left: 0;
    width: 100%;
    display: flex;
    justify-content: center;
    align-items: center;
    gap: 14px;
  }
  .brand-dot {
    width: 34px;
    height: 34px;
    border-radius: 50%;
    background: var(--green-dark);
  }
  .brand-name {
    font-weight: 700;
    font-size: 48px;
    letter-spacing: 2px;
    color: var(--green-dark);
  }
  .band {
    position: absolute;
    left: 0;
    top: 330px;
    width: 100%;
    height: 180px;
  }
  .band svg { display: block; }
  .product-name {
    position: absolute;
    left: 0;
    top: 362px;
    width: 100%;
    text-align: center;
    font-weight: 800;
    font-size: 74px;
    line-height: 1;
    color: var(--white);
    transform: rotate(-6deg);
  }
  .product-type {
    position: absolute;
    left: 0;
    top: 452px;
    width: 100%;
    text-align: center;
    font-weight: 600;
    font-size: 17px;
    letter-spacing: 0.5px;
    color: var(--white);
    transform: rotate(-3deg);
  }
  .tagline-vertical {
    position: absolute;
    left: 6px;
    top: 540px;
    width: 230px;
    transform-origin: left top;
    transform: rotate(-90deg) translateX(-230px);
    font-weight: 400;
    font-size: 24px;
    color: var(--faint);
    white-space: nowrap;
  }
  .natural-badge {
    position: absolute;
    left: 155px;
    top: 625px;
    width: 50px;
    height: 50px;
    border-radius: 50%;
    background: var(--green-dark);
    box-shadow: inset 0 0 0 3px var(--label), inset 0 0 0 5px var(--green-dark);
  }
  .natural-note {
    position: absolute;
    left: 0;
    top: 682px;
    width: 100%;
    text-align: center;
    font-size: 7px;
    line-height: 1.2;
    color: var(--white);
    text-transform: uppercase;
  }
  .net-volume {
    position: absolute;
    left: 0;
    top: 718px;
    width: 100%;
    text-align: center;
    font-weight: 600;
    font-size: 17px;
    color: var(--ink);
  }
</style>
</head>
<body>
  <div class="canvas">
    <div class="label">
      <div class="brand-mark">
        <span class="brand-dot"></span>
        <span class="brand-name">KOVA</span>
      </div>

      <div class="band">
        <svg width="360" height="180" viewBox="0 0 360 180" aria-hidden="true">
          <defs>
            <linearGradient id="bandGradient" x1="0" y1="1" x2="1" y2="0">
              <stop offset="0" stop-color="var(--green-band-start)"/>
              <stop offset="1" stop-color="var(--green-band-end)"/>
            </linearGradient>
          </defs>
          <path d="M0 40 Q180 25 360 0 L360 130 Q180 150 0 180 Z" fill="url(#bandGradient)"/>
        </svg>
      </div>
      <div class="product-name">Kova</div>
      <div class="product-type">NATURAL SKIN CREAM</div>

      <div class="tagline-vertical">Probiotic Skin Care</div>

      <div class="natural-badge"></div>
      <div class="natural-note">Made with all<br>natural ingredients</div>

      <div class="net-volume">Net Volume .50ml ℮</div>
    </div>
  </div>
</body>
</html>
```